Lone Prairie Canvas & Sound Jubilee

Organization:
Lone Prairie Canvas and Sound Jubilee is a non-profit organization created by a group of anonymous donors to bring more fun, culture, and art to a small Texas town. Our mission is to promote art and music in Washington County.
The multi-day eclectic festival will feature three stages, a film, art vendors, live mural artists, and food trucks set up throughout historic downtown Brenham. The event is FREE to the public.
Goals:
We need an attractive poster to publicize the festival.
Details:
Lone Prairie Canvas and Sound Jubilee
Friday, October 14 – 16
Free admission (VIP tickets available)
Live music- 3 stages/10 bands
Film Screening
Art vendors and art walk
Live art murals
Food trucks
www.loneprairiecanvasandsoundjubilee.example
#loneprairiecanvasandsound
Requirements:
Please incorporate our festival logo attached.
Conclusion:
After selecting a poster design, we hope to continue to work with the artist to design other event materials including website splash page and rack cards using design elements from the poster.

```html
<!DOCTYPE html>
<html lang="en">
<head>
<meta charset="utf-8">
<title>Lone Prairie Canvas and Sound Jubilee</title>
<link rel="stylesheet" href="https://fonts.googleapis.com/css2?family=Saira+Extra+Condensed:wght@400&family=Open+Sans:wght@400&display=swap">
<style>
  :root {
    --ink: #000000;
    --paper: #ffffff;
    --title: #fdfdc4;
    --pink: #f4b6c6;
    --sky: #b9d6f4;
    --mint: #a6efd6;
    --body: #ffffff;
  }
  html, body {
    margin: 0;
    padding: 0;
    width: 903px;
    height: 1200px;
    overflow: hidden;
    background: var(--ink);
  }
  .poster {
    position: relative;
    width: 903px;
    height: 1200px;
    background: var(--ink);
    overflow: hidden;
    font-family: "Open Sans", "Verdana", sans-serif;
    color: var(--body);
  }
  .guitar-body, .music-notes {
    position: absolute;
  }
  .guitar-body { left: 0; top: 0; }
  .music-notes { left: 640px; top: 560px; }
  .headline {
    position: absolute;
    left: 0;
    top: 0;
    margin: 0;
    font-weight: 400;
    font-size: inherit;
  }
  .headline svg { display: block; }
  .title-text {
    font-family: "Saira Extra Condensed", "Arial Narrow", sans-serif;
    font-variant: small-caps;
    fill: var(--title);
  }
  .dates-text {
    font-family: "Saira Extra Condensed", "Arial Narrow", sans-serif;
    font-size: 72px;
  }
  .dates-text .day { fill: var(--pink); }
  .dates-text .range { fill: var(--sky); }
  .admission {
    position: absolute;
    left: 70px;
    top: 506px;
    margin: 0;
  }
  .admission .free {
    display: block;
    font-size: 44px;
    color: var(--mint);
    letter-spacing: 1px;
    line-height: 1.1;
  }
  .admission .vip {
    display: block;
    font-size: 35px;
    color: var(--body);
    line-height: 1.25;
  }
  .highlights {
    position: absolute;
    left: 78px;
    top: 640px;
    margin: 0;
    padding: 0;
    list-style: none;
    font-size: 33px;
    line-height: 1.2;
  }
  .highlights li {
    position: relative;
    padding-left: 46px;
    margin-bottom: 30px;
  }
  .highlights li::before {
    content: "";
    position: absolute;
    left: 6px;
    top: 13px;
    width: 16px;
    height: 16px;
    border-radius: 50%;
    border: 3px solid var(--body);
  }
  .highlights .detail {
    display: block;
    font-size: 28px;
    padding-left: 2px;
  }
  .contact {
    position: absolute;
    left: 66px;
    top: 1080px;
    font-size: 16px;
    line-height: 1.8;
  }
  .contact p {
    margin: 0;
    position: relative;
    padding-left: 24px;
  }
  .contact p::before {
    content: "";
    position: absolute;
    left: 0;
    top: 9px;
    width: 11px;
    height: 11px;
    border-radius: 50%;
    background: var(--body);
  }
  .festival-mark {
    position: absolute;
    left: 590px;
    top: 1010px;
    width: 290px;
    display: flex;
    align-items: center;
    gap: 12px;
    color: var(--ink);
    font-size: 21px;
    line-height: 1.2;
  }
  .festival-mark .dot {
    flex: 0 0 34px;
    height: 34px;
    border-radius: 50%;
    background: var(--ink);
  }
</style>
</head>
<body>
<main class="poster">
  <svg class="guitar-body" width="903" height="1200" viewBox="0 0 903 1200" aria-hidden="true">
    <defs>
      <linearGradient id="note-haze" x1="0" y1="0" x2="1" y2="1">
        <stop offset="0" stop-color="#ffffff" stop-opacity="0"/>
        <stop offset="0.5" stop-color="#d6d6d6" stop-opacity="0.7"/>
        <stop offset="1" stop-color="#ffffff" stop-opacity="0"/>
      </linearGradient>
    </defs>
    <path d="M903 409 L624 588 C700 625 705 770 640 830 C600 875 565 915 548 960 L470 1200 L903 1200 Z" fill="#ffffff"/>
  </svg>
  <svg class="music-notes" width="263" height="380" viewBox="0 0 263 380" role="img" aria-label="Faint swirl of musical notes and staff lines">
    <path d="M60 40 L263 0 L263 380 L0 360 C70 280 90 220 60 40 Z" fill="url(#note-haze)"/>
  </svg>

  <h1 class="headline">
    <svg width="903" height="480" viewBox="0 0 903 480">
      <text class="title-text" x="451.5" y="214" text-anchor="middle" font-size="170" textLength="800" lengthAdjust="spacingAndGlyphs">Lone Prairie Canvas</text>
      <text class="title-text" x="451.5" y="346" text-anchor="middle" font-size="128" textLength="770" lengthAdjust="spacingAndGlyphs">and Sound Jubilee</text>
      <text class="dates-text" x="67" y="452" textLength="640" lengthAdjust="spacingAndGlyphs"><tspan class="day">Friday,</tspan> <tspan class="range">October 14 – 16</tspan></text>
    </svg>
  </h1>

  <p class="admission">
    <span class="free">FREE ADMISSION</span>
    <span class="vip">(VIP tickets available)</span>
  </p>

  <ul class="highlights">
    <li>Live music<span class="detail">3 stages/10 bands</span></li>
    <li>Film Screening</li>
    <li>Art vendors and art walk</li>
    <li>Live art murals</li>
    <li>Food trucks</li>
  </ul>

  <div class="contact">
    <p>www.loneprairiecanvasandsoundjubilee.example</p>
    <p>#loneprairiecanvasandsound</p>
  </div>

  <div class="festival-mark">
    <span class="dot"></span>
    <span class="name">Lone Prairie Canvas &amp; Sound Jubilee</span>
  </div>
</main>
</body>
</html>
```